Tolvek Consulting
Tolvek Consulting stationary
Tolvek Consulting - Consulting
Creative Brief
Professional
Daniel R. Tolvek
Chief Executive Officer
Tolvek Consulting, LLC P.O. Box 4372 Phoenix, AZ 85004
daniel@danielrtolvek-mail.com
danielrtolvek-mail.com
Tolvek Consulting Logo

```html
<!DOCTYPE html>
<html lang="en">
<head>
<meta charset="utf-8">
<title>Tolvek Consulting – Business Cards</title>
<link rel="stylesheet" href="https://fonts.googleapis.com/css2?family=Arimo:wght@400;700&display=swap">
<style>
  :root{
    --backdrop:#2b2b2d;
    --navy:#0d2748;
    --blue-mid:#1f4f73;
    --teal-glow:#3fb08f;
    --paper:#ffffff;
    --ink-navy:#1c3a6e;
    --orange:#f08a1c;
    --red:#e0262a;
    --black:#050505;
    --white:#ffffff;
  }
  *{margin:0;padding:0;box-sizing:border-box}
  html,body{width:1200px;height:732px;overflow:hidden;background:var(--backdrop)}
  body{position:relative;font-family:"Arimo",Arial,sans-serif}
  .card{position:absolute;width:569px;height:341px;border-radius:22px;overflow:hidden;box-shadow:0 6px 14px rgba(0,0,0,.45)}
  .card svg.card-art{position:absolute;inset:0;width:100%;height:100%}
  .card--front-full{left:19px;top:19px}
  .card--front-min{left:612px;top:19px}
  .card--dark{left:19px;top:379px}
  .card--dark-split{left:612px;top:379px}

  .brand{position:absolute;display:flex;flex-direction:column;align-items:center;font-family:"Arimo",Arial,sans-serif;font-weight:700;line-height:1}
  .brand__mark{width:46px;height:46px;background:currentColor;border-radius:6px;margin-bottom:14px}
  .brand__name{font-size:44px;letter-spacing:1px}
  .brand__sub{font-size:17px;letter-spacing:6px;margin-top:4px}
  .brand--navy{color:var(--ink-navy)}
  .brand--white{color:var(--white)}

  .person{position:absolute;right:34px;top:26px;text-align:right}
  .person__name{color:var(--red);font-weight:700;font-size:15px}
  .person__title{color:var(--white);font-size:14px;margin-top:2px}

  .contact{position:absolute;right:34px;top:192px;text-align:right;color:var(--white);font-size:13.5px;line-height:17px}
  .contact__line{display:flex;justify-content:flex-end;align-items:center;gap:6px}
  .contact__icon{width:9px;height:9px;fill:var(--red)}

  .web{position:absolute;color:var(--white);font-size:13.5px}
  .web__label{color:var(--red);font-weight:700}
</style>
</head>
<body>

<!-- Card 1: full front -->
<section class="card card--front-full">
  <svg class="card-art" viewBox="0 0 569 341" aria-hidden="true">
    <defs>
      <radialGradient id="glowA" cx="62%" cy="48%" r="60%">
        <stop offset="0" stop-color="var(--teal-glow)"/>
        <stop offset=".45" stop-color="var(--blue-mid)"/>
        <stop offset="1" stop-color="var(--navy)"/>
      </radialGradient>
    </defs>
    <rect width="569" height="341" fill="url(#glowA)"/>
    <path d="M0 0H255Q345 170 238 341H0Z" fill="var(--paper)"/>
    <path d="M268 118Q305 228 236 334" fill="none" stroke="var(--orange)" stroke-width="7" stroke-linecap="round"/>
  </svg>
  <div class="brand brand--navy" style="left:24px;top:122px;width:210px">
    <span class="brand__mark"></span>
    <span class="brand__name">TOLVEK</span>
    <span class="brand__sub">CONSULTING</span>
  </div>
  <div class="person">
    <div class="person__name">Daniel R. Tolvek</div>
    <div class="person__title">Chief Executive Officer</div>
  </div>
  <div class="contact">
    <div>Tolvek Consulting, LLC</div>
    <div>P.O. Box 4372</div>
    <div>Phoenix, AZ 85004</div>
    <div class="contact__line"><svg class="contact__icon" viewBox="0 0 10 10"><circle cx="5" cy="5" r="5"/></svg>480.555.0172</div>
    <div class="contact__line"><svg class="contact__icon" viewBox="0 0 10 10"><circle cx="5" cy="5" r="5"/></svg>daniel@danielrtolvek-mail.com</div>
    <div class="contact__line"><span class="web__label">W:</span>danielrtolvek-mail.com</div>
  </div>
</section>

<!-- Card 2: minimal front -->
<section class="card card--front-min">
  <svg class="card-art" viewBox="0 0 569 341" aria-hidden="true">
    <defs>
      <radialGradient id="glowB" cx="62%" cy="48%" r="60%">
        <stop offset="0" stop-color="var(--teal-glow)"/>
        <stop offset=".45" stop-color="var(--blue-mid)"/>
        <stop offset="1" stop-color="var(--navy)"/>
      </radialGradient>
    </defs>
    <rect width="569" height="341" fill="url(#glowB)"/>
    <path d="M0 0H255Q345 170 238 341H0Z" fill="var(--paper)"/>
    <path d="M268 118Q305 228 236 334" fill="none" stroke="var(--orange)" stroke-width="7" stroke-linecap="round"/>
  </svg>
  <div class="brand brand--navy" style="left:24px;top:122px;width:210px">
    <span class="brand__mark"></span>
    <span class="brand__name">TOLVEK</span>
    <span class="brand__sub">CONSULTING</span>
  </div>
  <div class="web" style="right:34px;bottom:18px"><span class="web__label">W:</span> danielrtolvek-mail.com</div>
</section>

<!-- Card 3: dark -->
<section class="card card--dark">
  <svg class="card-art" viewBox="0 0 569 341" aria-hidden="true">
    <rect width="569" height="341" fill="var(--black)"/>
  </svg>
  <div class="brand brand--white" style="left:0;right:0;top:118px">
    <span class="brand__mark"></span>
    <span class="brand__name">TOLVEK</span>
    <span class="brand__sub">CONSULTING</span>
  </div>
  <div class="web" style="left:168px;bottom:18px"><span class="web__label">W:</span> danielrtolvek-mail.com</div>
</section>

<!-- Card 4: dark split -->
<section class="card card--dark-split">
  <svg class="card-art" viewBox="0 0 569 341" aria-hidden="true">
    <defs>
      <radialGradient id="glowC" cx="68%" cy="45%" r="55%">
        <stop offset="0" stop-color="var(--teal-glow)"/>
        <stop offset=".45" stop-color="var(--blue-mid)"/>
        <stop offset="1" stop-color="var(--navy)"/>
      </radialGradient>
    </defs>
    <rect width="569" height="341" fill="url(#glowC)"/>
    <path d="M0 0H300Q225 170 292 341H0Z" fill="var(--black)"/>
    <path d="M252 178Q232 282 300 336" fill="none" stroke="var(--orange)" stroke-width="7" stroke-linecap="round"/>
  </svg>
  <div class="brand brand--white" style="left:22px;top:128px;width:210px">
    <span class="brand__mark"></span>
    <span class="brand__name">TOLVEK</span>
    <span class="brand__sub">CONSULTING</span>
  </div>
  <div class="web" style="left:318px;bottom:18px"><span class="web__label">W:</span> danielrtolvek-mail.com</div>
</section>

</body>
</html>
```